NEW YORK Plumbing/utility company 10 year anniversary business card

Looking For simple back and front business card would like to include a few things in description
We offer 24/7 emergency service
residential
commercial
industrial
municipal
services offered
Plumbing
hydro excavation
hydro jetting
Well pumps
Sewer pumps
water mains
sewer mains

```html
<!DOCTYPE html>
<html lang="en">
<head>
<meta charset="utf-8">
<title>Ridgeline Water &amp; Sewer – Business Card</title>
<link href="https://fonts.googleapis.com/css2?family=Montserrat:wght@400;500;600;700&display=swap" rel="stylesheet">
<style>
  :root {
    --page: #e9ebee;
    --navy: #0b5996;
    --deep: #0a4f87;
    --sky: #1fa8ec;
    --sky-soft: #3cbcf5;
    --ink: #2b2f36;
    --white: #ffffff;
  }
  * { box-sizing: border-box; margin: 0; padding: 0; }
  html, body { width: 1200px; height: 1200px; overflow: hidden; }
  body {
    background: var(--page);
    font-family: "Montserrat", sans-serif;
    position: relative;
  }
  .card {
    position: absolute;
    left: 160px;
    width: 880px;
    height: 503px;
    border-radius: 34px;
    overflow: hidden;
    box-shadow: 0 10px 28px rgba(0,0,0,.18);
  }

  /* Front */
  .card-front { top: 72px; background: var(--white); }
  .front-band {
    position: absolute; left: 0; right: 0; bottom: 0; height: 175px;
    background: var(--navy);
    border-top: 8px solid var(--sky);
  }
  .identity {
    position: absolute; left: 58px; top: 96px;
    padding-left: 22px;
    border-left: 7px solid var(--sky);
  }
  .person-name {
    font-weight: 600; font-size: 46px; color: var(--sky);
    letter-spacing: 1px; line-height: 1;
  }
  .person-title {
    font-weight: 500; font-size: 17px; color: var(--ink);
    margin-top: 6px; letter-spacing: .5px;
  }
  .contacts { position: absolute; left: 62px; top: 200px; list-style: none; }
  .contacts li {
    display: flex; align-items: center; gap: 16px;
    font-size: 24px; font-weight: 500; color: var(--ink);
    height: 40px;
  }
  .contacts svg { width: 24px; height: 24px; fill: var(--sky); flex: none; }
  .brand {
    position: absolute; right: 70px; top: 92px;
    display: flex; align-items: center; gap: 16px;
    color: var(--deep); font-weight: 700; text-align: left;
  }
  .brand-dot { width: 26px; height: 26px; border-radius: 50%; background: var(--deep); flex: none; }
  .brand-name { font-size: 40px; line-height: 1.05; letter-spacing: 2px; }
  .brand-name small { display: block; font-size: 22px; letter-spacing: 4px; margin-top: 6px; }
  .services {
    position: absolute; left: 0; right: 0; top: 22px;
    text-align: center; color: var(--white);
  }
  .services-heading {
    font-weight: 600; font-size: 22px; color: var(--sky-soft);
    letter-spacing: 1px; margin-bottom: 10px;
  }
  .services-list { font-size: 21px; font-weight: 500; line-height: 1.45; }
  .services-list .sep { color: var(--sky-soft); margin: 0 6px; }

  /* Back */
  .card-back { top: 625px; background: linear-gradient(160deg, #0d5d9c 0%, var(--navy) 55%, var(--deep) 100%); }
  .brand-back {
    position: absolute; left: 0; right: 0; top: 110px;
    display: flex; justify-content: center; align-items: center; gap: 20px;
    color: var(--white); font-weight: 700;
  }
  .brand-back .brand-dot { width: 34px; height: 34px; background: var(--white); }
  .brand-back .brand-name { font-size: 58px; letter-spacing: 3px; }
  .brand-back .brand-name small { font-size: 30px; letter-spacing: 6px; }
  .tagline {
    position: absolute; left: 0; right: 0; top: 318px; text-align: center;
  }
  .tagline-emergency { font-size: 28px; font-weight: 600; color: var(--sky-soft); }
  .tagline-sectors { font-size: 28px; font-weight: 600; color: var(--white); margin-top: 10px; }
  .back-strip {
    position: absolute; right: 0; bottom: 0; width: 62%; height: 26px;
    background: var(--sky-soft);
  }
</style>
</head>
<body>

<section class="card card-front" aria-label="Business card front">
  <div class="identity">
    <p class="person-name">SAM CARTER</p>
    <p class="person-title">CEO | FOUNDER</p>
  </div>
  <ul class="contacts">
    <li>
      <svg viewBox="0 0 24 24" aria-hidden="true"><path d="M6.6 10.8a15.1 15.1 0 0 0 6.6 6.6l2.2-2.2a1 1 0 0 1 1-.25 11.4 11.4 0 0 0 3.6.57 1 1 0 0 1 1 1V20a1 1 0 0 1-1 1A17 17 0 0 1 3 4a1 1 0 0 1 1-1h3.5a1 1 0 0 1 1 1c0 1.25.2 2.45.57 3.57a1 1 0 0 1-.25 1z"/></svg>
      555-014-2290
    </li>
    <li>
      <svg viewBox="0 0 24 24" aria-hidden="true"><path d="M12 2a10 10 0 1 0 0 20 10 10 0 0 0 0-20zm6.9 6h-2.9a15.7 15.7 0 0 0-1.4-3.6A8 8 0 0 1 18.9 8zM12 4c.8 1.2 1.5 2.5 1.9 4h-3.8c.4-1.5 1.1-2.8 1.9-4zM4.3 14a8 8 0 0 1 0-4h3.4a16.5 16.5 0 0 0 0 4zm.8 2H8c.3 1.3.8 2.5 1.4 3.6A8 8 0 0 1 5.1 16zM8 8H5.1a8 8 0 0 1 4.3-3.6C8.8 5.5 8.3 6.7 8 8zm4 12c-.8-1.2-1.5-2.5-1.9-4h3.8c-.4 1.5-1.1 2.8-1.9 4zm2.3-6H9.7a14.7 14.7 0 0 1 0-4h4.6a14.7 14.7 0 0 1 0 4zm.3 5.6c.6-1.1 1.1-2.3 1.4-3.6h2.9a8 8 0 0 1-4.3 3.6zm1.7-5.6a16.5 16.5 0 0 0 0-4h3.4a8 8 0 0 1 0 4z"/></svg>
      www.ridgelinews.com
    </li>
    <li>
      <svg viewBox="0 0 24 24" aria-hidden="true"><path d="M2 5h20v14H2zm2 2v.5l8 5 8-5V7zm0 2.8V17h16V9.8l-8 5z"/></svg>
      info@ridgelinews.com
    </li>
  </ul>
  <div class="brand">
    <span class="brand-dot" aria-hidden="true"></span>
    <p class="brand-name">RIDGELINE<small>WATER &amp; SEWER</small></p>
  </div>
  <div class="front-band">
    <div class="services">
      <p class="services-heading">SERVICES OFFERED</p>
      <p class="services-list">Plumbing<span class="sep">•</span>Hydro excavation<span class="sep">•</span>Hydro jetting<span class="sep">•</span>Well pumps<br>Sewer pumps<span class="sep">•</span>Water mains<span class="sep">•</span>Sewer mains</p>
    </div>
  </div>
</section>

<section class="card card-back" aria-label="Business card back">
  <div class="brand-back">
    <span class="brand-dot" aria-hidden="true"></span>
    <p class="brand-name">RIDGELINE<small>WATER &amp; SEWER</small></p>
  </div>
  <div class="tagline">
    <p class="tagline-emergency">Emergency Plumbing Service 24/7</p>
    <p class="tagline-sectors">Residential - Commercial - Industrial - Municipal</p>
  </div>
  <div class="back-strip" aria-hidden="true"></div>
</section>

</body>
</html>
```